New website design and logo for FusoBrite.com to help ignite the website sales.

Hi designers,

Fusobrite is a new welding brand that is selling welding equipement.

Currently I have around 5 to 10 products. The issue is that the site itself does not do that much of sales. So I have to do something about the seo etc. but that is out of scope for the design.

What is in scope is to comeup with a new logo and website look and feel that is in line with the customers.

men, non professionals, garage, home improvements, perhaps sme ( small mediul entreprice business that want to start in the welding industry.

Products are midrange prices and quality. The look and feel must breath cool stuff, sexy ( women in working cloths carrying welding gloves, other protection gear and weldels)

The wedsite is build in wordpress with the Divi theme. I am an IT guy myself withhout any creativity in me :( so if you can help me with that that would be great.

Please have a quick look at fusobrite.com

Best regards,
Joost

Target Market(s)

non professional welders that do metal work in there garage

Coding

Coded - Design and coding required

Number of Pages Required

3 page

Font styles to use
Sans Serif

Colors
0355a3
ffc214

Requirements
Must have
• I would like to see a new homepage and product page design together with a new logo.
Nice to have
• shop design

```html
<!DOCTYPE html>
<html lang="en">
<head>
<meta charset="utf-8">
<title>Fusobrite – Welding equipment</title>
<link href="https://fonts.googleapis.com/css2?family=Montserrat:wght@500;600;700;800&family=Open+Sans:wght@400;600;700&display=swap" rel="stylesheet">
<style>
  :root{
    --blue:#0355a3;
    --blue-dark:#023f7a;
    --blue-light:#1b8ff0;
    --yellow:#ffc214;
    --ink:#222;
    --muted:#777;
    --line:#d9d9d9;
    --white:#fff;
  }
  *{box-sizing:border-box;margin:0;padding:0}
  html,body{width:1200px;height:2424px;overflow:hidden}
  body{font-family:"Open Sans",Arial,sans-serif;color:var(--ink);background:var(--white);position:relative}

  .topbar{height:32px;background:var(--blue);color:var(--white);font-size:12px;font-weight:600;
    display:flex;justify-content:space-between;align-items:center;padding:0 108px}

  .site-header{height:108px;background:var(--white);position:relative;display:flex;align-items:center;box-shadow:0 2px 6px rgba(0,0,0,.08);z-index:2}
  .brand{position:absolute;left:108px;top:50%;transform:translateY(-50%);display:flex;align-items:center;gap:12px;
    font-family:"Montserrat",sans-serif;font-weight:800;font-size:24px;color:var(--blue)}
  .brand-dot{width:34px;height:34px;border-radius:50%;background:var(--yellow)}
  .main-nav{position:absolute;left:348px;display:flex;gap:46px;font-family:"Montserrat",sans-serif;font-weight:600;font-size:14px;letter-spacing:.5px}
  .main-nav a{color:var(--ink);text-decoration:none;padding-bottom:8px}
  .main-nav a.active{color:var(--blue);border-bottom:3px solid var(--blue)}
  .cart{position:absolute;left:890px;display:flex;align-items:center;gap:12px;font-family:"Montserrat",sans-serif;font-weight:600;font-size:14px}
  .cart-icon{width:40px;height:40px;border-radius:50%;background:var(--yellow);display:flex;align-items:center;justify-content:center}

  .hero{position:relative;height:560px;
    background:radial-gradient(circle at 78% 55%,#f6c25a 0,#c5762a 12%,#3a3226 30%,#16202b 55%,#0c1520 100%)}
  .hero-copy{position:absolute;left:48px;top:178px;width:640px;color:var(--white)}
  .hero-copy h1{font-family:"Montserrat",sans-serif;font-weight:700;font-size:38px;line-height:1.2;text-transform:uppercase}
  .hero-copy p{margin-top:14px;font-family:"Montserrat",sans-serif;font-weight:600;font-size:28px;color:var(--blue-light)}
  .hero-dots{position:absolute;left:48px;bottom:40px;display:flex;gap:8px}
  .hero-dots span{width:10px;height:10px;border-radius:50%;background:rgba(255,255,255,.55)}
  .hero-dots span:first-child{background:var(--white)}

  .featured{padding-top:96px}
  .featured h2{text-align:center;font-family:"Montserrat",sans-serif;font-weight:600;font-size:38px;letter-spacing:1px;color:#333}
  .product-grid{margin:48px auto 0;width:984px;display:grid;grid-template-columns:repeat(3,312px);gap:40px 24px}
  .product-card{height:328px;border:1px solid var(--line);text-align:center;padding:20px 16px}
  .product-photo{width:200px;height:200px;margin:0 auto;border-radius:4px}
  .product-name{margin-top:22px;font-family:"Montserrat",sans-serif;font-weight:600;font-size:15px;text-transform:uppercase}
  .product-price{margin-top:10px;font-weight:700;font-size:15px;color:var(--blue-light)}
  .product-price del{color:#999;font-weight:600;margin-right:8px}

  .site-footer{position:absolute;left:0;top:2040px;width:1200px;height:384px;color:var(--white);
    background:linear-gradient(180deg,#0b6ad0 0%,var(--blue) 60%,var(--blue-dark) 100%)}
  .footer-cols{display:flex;padding:128px 108px 0}
  .footer-cols h3{font-family:"Montserrat",sans-serif;font-weight:700;font-size:17px;margin-bottom:16px;text-transform:uppercase}
  .footer-about{width:330px;font-size:13px;line-height:1.6}
  .footer-links{margin-left:72px;width:360px}
  .footer-links .cols{display:flex;gap:70px}
  .footer-cols ul{list-style:none;font-size:13px;line-height:1.75}
  .footer-cols li::before{content:"•";color:var(--yellow);margin-right:8px}
  .footer-social{margin-left:auto;width:170px}
  .footer-bottom{position:absolute;left:0;right:0;bottom:28px;text-align:center;font-size:12px}
  .footer-bottom .currency{position:absolute;right:108px}
</style>
</head>
<body>
  <div class="topbar">
    <span>Lorem ipsum dolor sit amet, consectetur adipiscing elit, sed do eiusmod</span>
    <span>Call us Today : +31(0)20 555 0142</span>
  </div>

  <header class="site-header">
    <div class="brand"><span class="brand-dot"></span>Fusobrite</div>
    <nav class="main-nav">
      <a class="active" href="#">HOME</a>
      <a href="#">PRODUCTS</a>
      <a href="#">WINKELMAND</a>
      <a href="#">MIJN ACCOUNT</a>
    </nav>
    <div class="cart">
      <span class="cart-icon">
        <svg width="20" height="20" viewBox="0 0 24 24" fill="none" stroke="#fff" stroke-width="2"><path d="M3 4h2l2.4 10.5h10.8L21 7H6.5"/><circle cx="9" cy="19" r="1.6"/><circle cx="17" cy="19" r="1.6"/></svg>
      </span>
      CART : € 0.00
    </div>
  </header>

  <section class="hero" role="img" aria-label="Welder in protective gloves working with sparks flying">
    <div class="hero-copy">
      <h1>Simple welding of steel and aluminum get great results with tools that work</h1>
      <p>Free shipping from € 30.00</p>
    </div>
    <div class="hero-dots"><span></span><span></span><span></span></div>
  </section>

  <section class="featured">
    <h2>FEATURED PRODUCT</h2>
    <div class="product-grid">
      <article class="product-card">
        <div class="product-photo" role="img" aria-label="Red and black welding machine" style="background:linear-gradient(135deg,#d23a2c,#3a3a3a)"></div>
        <div class="product-name">TX-250P</div>
        <div class="product-price"><del>€ 845.00</del>€ 795.00</div>
      </article>
      <article class="product-card">
        <div class="product-photo" role="img" aria-label="Blue and white welding machine" style="background:linear-gradient(135deg,#dfe6ee,#2c6fc0)"></div>
        <div class="product-name">TX-250S</div>
        <div class="product-price">€ 745.00</div>
      </article>
      <article class="product-card">
        <div class="product-photo" role="img" aria-label="Black welding helmet with 180 degree view" style="background:linear-gradient(135deg,#5a5a5a,#1c1c1c)"></div>
        <div class="product-name">Welding helmet 180 degrees view</div>
        <div class="product-price">€ 109.00</div>
      </article>
      <article class="product-card">
        <div class="product-photo" role="img" aria-label="Black welding helmet with large view window" style="background:linear-gradient(135deg,#4e4e4e,#151515)"></div>
        <div class="product-name">Welding helmet large view</div>
        <div class="product-price">€ 89.00</div>
      </article>
      <article class="product-card">
        <div class="product-photo" role="img" aria-label="Large wooden measuring triangle" style="background:linear-gradient(135deg,#c9a070,#6b4a2c)"></div>
        <div class="product-name">Large measuring triangle</div>
        <div class="product-price"><del>€ 33.50</del>€ 25.00</div>
      </article>
      <article class="product-card">
        <div class="product-photo" role="img" aria-label="Blue and yellow leather welding gloves" style="background:linear-gradient(135deg,#f2c14a,#2a5fb8)"></div>
        <div class="product-name">Welding gloves blue</div>
        <div class="product-price">€ 22.40</div>
      </article>
      <article class="product-card">
        <div class="product-photo" role="img" aria-label="Black leather welding gloves" style="background:linear-gradient(135deg,#6a6a5c,#1d1d1a)"></div>
        <div class="product-name">Welding gloves black</div>
        <div class="product-price">€ 22.40</div>
      </article>
      <article class="product-card">
        <div class="product-photo" role="img" aria-label="Small wooden measuring triangle" style="background:linear-gradient(135deg,#d0a878,#70502f)"></div>
        <div class="product-name">Small measuring triangle</div>
        <div class="product-price">€ 17.25</div>
      </article>
    </div>
  </section>

  <footer class="site-footer">
    <div class="footer-cols">
      <div class="footer-about">
        <h3>Fusobrite</h3>
        <p>Lorem ipsum dolor sit amet consectetur adipiscing elit sed do eiusmod tempor incididunt ut labore et dolore magna aliqua. Ut enim ad minim veniam quis nostrud.</p>
      </div>
      <div class="footer-links">
        <h3>Quick links</h3>
        <div class="cols">
          <ul><li>Home</li><li>About</li><li>Contact</li><li>Customer care</li><li>Information</li></ul>
          <ul><li>Installation</li><li>Sources</li><li>Privacy policy</li><li>Returns</li></ul>
        </div>
      </div>
      <div class="footer-social">
        <h3>Follow us</h3>
        <ul><li>Facebook</li><li>Instagram</li><li>Twitter</li><li>LinkedIn</li></ul>
      </div>
    </div>
    <div class="footer-bottom">
      Copyright © 2021 Company name | Privacy Policy | Terms &amp; Conditions | Contact | Sitemap
      <span class="currency">EUR</span>
    </div>
  </footer>
</body>
</html>
```